Book Cover Design for a Romantic Comedy Novel

Hi there,

we are two German authors planning to digitally publish our first novel. In order to draw a lot of attention to our e-book we need an eye-catching cover design. That is where we need your help!

Here is the novel's synopsis:
Marie, a 29-year-old business analyst from Stuttgart, knows exactly what the man of her life should not be like: no colleague, no workaholic, no smoker and nobody with a tattoo. When she learns that her ex-boyfriend is going to marry, she throws all her caution overboard and spends the night with a man she has just met. Monday morning she is in for a surprise: her one-time lover turns out to be her new colleague! And in every other aspect, too, Karlo seems to be the embodiment of Marie's no-go-list.

The character's looks: Marie is tall, has long red curls and light skin. Karlo is also tall and has very short light brown hair.

The title of the book is "Vergessen verzaubert" which cannot be translated into English without losing some of its meaning.

While "verliebt" is best translated with "in love", the German word "verplant" has two meanings:
a) over-scheduled, making too many plans (Marie loves to make plans and to write lists like her no-go-list, to-do-lists ...)
b) to be out of it (Marie does not recognize her Mr Perfect when he stands right before her eyes)

Our names should also be on the cover: Annika Falter & Henriette Dussel

Please note the technical requirements below.

We are looking forward to your great designs.
Thanks
Annika & Henriette
Updates

Hi there, we just added some book covers to our project in order to show you the kind of design we generally like. Of course, we do not want to limit your creativity - so feel free to post something different. Furthermore, we added some details on the look of our main characters in case you want to show them on your cover. Thank you very much for your contributions so far! BR Henriette & Annika

Target Market(s)

Women aged 25 to 40

Industry/Entity Type

Business

Requirements
Must have
• This is a book for women, romantic, funny & smart. So please stick to the genre, the cover has to show on first glance what to expect.

Technical requirements:

1. The cover needs to be legible and good-looking when it is reduced to a small icon the size of a stamp. This will be the case when the book cover is shown in a list with lots of other book covers.

2. The design should be in colour, but it should also work in black and white as a lot of e-book readers do not display colours.

3. We need a jpeg with the following measurements: ratio = 16:10, the longer side with at least 2500 pixel.

4. As we want to publish our book in several online bookstores and maybe one day as a printed version, we ask you to provide us the original photoshop-file. Each digital bookstore has different requirements with regards to file size and width-to-heigth-ratio. Therefore, the cover design should be scalable to different ratios.

Should not have
• We do not want a book cover based on a real photograph.

```html
<!DOCTYPE html>
<html lang="de">
<head>
<meta charset="utf-8">
<title>Vergessen verzaubert – Buchcover</title>
<link rel="stylesheet" href="https://fonts.googleapis.com/css2?family=Gochi+Hand&family=Handlee&display=swap">
<style>
  :root {
    --sky: #06c9e6;
    --ink: #2b2b2b;
    --heart-red: #e0262a;
    --heart-pink: #e8336a;
    --heart-orange: #ef6a24;
    --scribble: #d81f2a;
    --title-ink: #111111;
    --title-halo: #ffffff;
  }
  html, body {
    margin: 0;
    padding: 0;
    overflow: hidden;
    background: var(--sky);
  }
  .cover {
    position: relative;
    width: 702px;
    height: 1200px;
    overflow: hidden;
    background: var(--sky);
  }
  .cover-art {
    position: absolute;
    inset: 0;
    width: 702px;
    height: 1200px;
  }
  .grid line {
    stroke: var(--ink);
    stroke-width: 2.4;
    stroke-linecap: round;
  }
  .heart-outline {
    fill: none;
    stroke: var(--scribble);
    stroke-width: 2;
    opacity: 0.85;
  }
  .authors {
    position: absolute;
    top: 6px;
    left: 0;
    width: 702px;
    margin: 0;
    text-align: center;
    font-family: "Gochi Hand", cursive;
    font-weight: 400;
    font-size: 39px;
    letter-spacing: 1px;
    color: var(--ink);
  }
  .title {
    position: absolute;
    top: 470px;
    left: 70px;
    width: 540px;
    margin: 0;
    text-align: center;
    font-family: "Handlee", cursive;
    font-weight: 400;
    font-size: 58px;
    line-height: 1;
    color: var(--title-ink);
    transform: rotate(-9deg);
    transform-origin: center;
    text-shadow:
      3px 3px 0 var(--title-halo),
      2px 2px 0 var(--title-halo),
      -1px -1px 0 var(--title-halo);
  }
</style>
</head>
<body>
<main class="cover">
  <svg class="cover-art" viewBox="0 0 702 1200" xmlns="http://www.w3.org/2000/svg">
    <defs>
      <linearGradient id="heartFill" x1="0" y1="0" x2="1" y2="1">
        <stop offset="0" stop-color="var(--heart-orange)"/>
        <stop offset="0.45" stop-color="var(--heart-red)"/>
        <stop offset="1" stop-color="var(--heart-pink)"/>
      </linearGradient>
    </defs>

    <g class="grid">
      <line x1="5" y1="0" x2="6" y2="1200"/>
      <line x1="31" y1="0" x2="29" y2="1200"/>
      <line x1="57" y1="0" x2="59" y2="1200"/>
      <line x1="79" y1="0" x2="77" y2="1200"/>
      <line x1="236" y1="0" x2="238" y2="1200"/>
      <line x1="462" y1="0" x2="460" y2="1200"/>
      <line x1="492" y1="0" x2="494" y2="1200"/>
      <line x1="579" y1="0" x2="577" y2="1200"/>
      <line x1="640" y1="0" x2="642" y2="1200"/>
      <line x1="668" y1="0" x2="667" y2="1200"/>
      <line x1="692" y1="0" x2="694" y2="1200"/>

      <line x1="0" y1="14" x2="702" y2="12"/>
      <line x1="0" y1="52" x2="702" y2="54"/>
      <line x1="0" y1="66" x2="702" y2="65"/>
      <line x1="0" y1="125" x2="702" y2="127"/>
      <line x1="0" y1="168" x2="702" y2="166"/>
      <line x1="0" y1="226" x2="702" y2="224"/>
      <line x1="0" y1="278" x2="702" y2="280"/>
      <line x1="0" y1="306" x2="702" y2="304"/>
      <line x1="0" y1="486" x2="702" y2="484"/>
      <line x1="0" y1="600" x2="702" y2="602"/>
      <line x1="0" y1="636" x2="702" y2="634"/>
      <line x1="0" y1="662" x2="702" y2="664"/>
      <line x1="0" y1="880" x2="702" y2="878"/>
      <line x1="0" y1="932" x2="702" y2="934"/>
      <line x1="0" y1="1010" x2="702" y2="1008"/>
      <line x1="0" y1="1096" x2="702" y2="1098"/>
      <line x1="0" y1="1130" x2="702" y2="1128"/>
      <line x1="0" y1="1180" x2="702" y2="1182"/>
    </g>

    <path class="heart-outline"
          d="M360 320 C340 230 250 205 160 225 C60 250 20 350 30 450 C50 620 170 790 200 990
             C280 820 440 690 560 590 C650 510 700 390 670 290 C640 200 470 180 360 320 Z"/>

    <path class="heart" role="img" aria-label="Heart filled with a repeating butterfly pattern in red, pink and orange"
          fill="url(#heartFill)"
          d="M345 330 C320 250 220 235 150 255 C60 280 30 370 45 460 C70 620 170 780 190 945
             C260 800 420 660 520 560 C600 480 640 380 610 290 C580 215 440 200 345 330 Z"/>
  </svg>

  <p class="authors">Annika Falter &amp; Henriette Dussel</p>
  <h1 class="title">Vergessen verzaubert</h1>
</main>
</body>
</html>
```